Web Design for a Biotech Consulting Firm

We need a web site design for a new business based in Philadelphia called Corventa Dx. This is a consulting firm that will serve medical diagnostics industry, which is part of the life science/healthcare industry focusing on developing and marketing products that help in early detection, monitoring or management of diseases. Our consulting firm will help medical diagnostic companies to overcome key challenges in designing, evaluating and marketing new products.Our company name is Corventa Dx. Corventa is Latin word for "something" Dx represents diagnostics. The idea behind the name is that we help companies to transform the original, early product ideas ("nothing") into "something"; which is a product with full clinical utility that will help to improve health and well-being.The web site should use the visual feel of the logo (attached), be modern, simple and clean looking and represent creativity, innovation, scientific thinking and progress.
Updates

Wix Design is acceptable

Industry/Entity Type

Biotechnology

Coding

Coded - Design and coding required

Number of Pages Required

1 page

Font styles to use
Sans Serif

Requirements
Must have
• simple, clean look couple of pages
Should not have
• a lot of pages

```html
<!DOCTYPE html>
<html lang="en">
<head>
<meta charset="utf-8">
<title>Corventa Dx — Biotech Consulting</title>
<link href="https://fonts.googleapis.com/css2?family=Lato:wght@400;700&family=Montserrat:wght@300;400;500;600;700&display=swap" rel="stylesheet">
<style>
:root{
  --blue:#2f86ea;
  --ink:#1c1c1c;
  --text:#2a2a2a;
  --footer:#121212;
  --white:#fff;
}
*{margin:0;padding:0;box-sizing:border-box}
html,body{width:1200px;height:3019px;overflow:hidden;background:var(--white)}
body{position:relative;font-family:'Lato',sans-serif;color:var(--text)}

/* header */
.site-header{position:absolute;left:0;top:0;width:1200px;height:110px;background:var(--white)}
.brand{position:absolute;left:115px;top:40px;height:24px;display:flex;align-items:center;gap:10px}
.brand i{display:block;width:14px;height:14px;background:var(--blue)}
.brand span{font-family:'Montserrat',sans-serif;font-size:19px;font-weight:500;color:var(--ink);white-space:nowrap}
.nav a{position:absolute;top:52px;font-family:'Montserrat',sans-serif;font-size:14px;color:var(--ink);text-decoration:none}
.nav a.active{color:var(--blue);border:1px solid var(--blue);padding:4px 7px;top:47px}
.header-divider{position:absolute;left:897px;top:20px;width:1px;height:70px;background:#e3e3e3}
.call-label{position:absolute;left:946px;top:30px;font-family:'Montserrat',sans-serif;font-size:17px;letter-spacing:1px;color:var(--ink);border-bottom:2px solid var(--ink);padding-bottom:4px}
.call-phone{position:absolute;left:940px;top:60px;font-family:'Montserrat',sans-serif;font-size:21px;font-weight:600;color:var(--blue)}

/* hero */
.hero{position:absolute;left:0;top:110px;width:1200px;height:563px;background:linear-gradient(110deg,#d7e4f5 0%,#5e8fd8 30%,#2d5fc4 60%,#1d3f97 100%)}
.hero h1{position:absolute;left:115px;top:200px;font-family:'Montserrat',sans-serif;font-size:34px;font-weight:700;line-height:43px;color:#111;width:560px}
.hero-arrow{position:absolute;top:352px;width:28px;height:26px;border:1px solid #222;background:rgba(255,255,255,.85)}
.hero-arrow svg{position:absolute;left:8px;top:7px}

/* section headings */
.sec-title{position:absolute;left:0;width:1200px;text-align:center;font-family:'Montserrat',sans-serif;font-weight:400;font-size:33px;letter-spacing:.5px;color:var(--ink)}
.sec-title em{font-style:normal;color:var(--blue)}
.rule{position:absolute;left:534px;width:132px;height:3px}
.rule i{position:absolute;top:0;width:66px;height:3px}
.rule i:first-child{left:0;background:var(--ink)}
.rule i:last-child{left:66px;background:var(--blue)}

/* welcome */
.lead{position:absolute;left:0;width:1200px;text-align:center;color:var(--blue);font-size:15px;line-height:23px}
.body-copy{position:absolute;left:145px;width:910px;text-align:center;font-size:13.5px;line-height:22.5px;color:#222}
.pillar-icon{position:absolute;width:65px;height:65px;border:2px solid var(--blue)}
.pillar-title{position:absolute;font-family:'Montserrat',sans-serif;font-weight:600;font-size:17px;color:#111}
.pillar-text{position:absolute;font-size:13.5px;line-height:23px;color:#222;width:320px}
.pillar-text em{font-style:normal;color:var(--blue)}

/* services */
.services{position:absolute;left:0;top:1138px;width:1200px;height:543px;background:linear-gradient(180deg,#3a8cea,#4796ee)}
.services .sec-title{top:80px;color:#1c1c1c}
.services .sec-title em{color:var(--white)}
.services .rule i:last-child{background:#a9cdf6}
.services .sub{position:absolute;top:152px;width:1200px;text-align:center;color:var(--white);font-size:16px}
.service{position:absolute;top:222px;width:300px;text-align:center;color:var(--white)}
.service svg{display:block;margin:0 auto}
.service h3{margin-top:30px;font-family:'Montserrat',sans-serif;font-weight:700;font-size:19px;letter-spacing:.5px}
.service p{margin-top:16px;font-size:13.5px;line-height:22px}
.btn-outline{display:inline-block;margin-top:24px;padding:8px 14px;border:1px solid var(--white);font-family:'Montserrat',sans-serif;font-size:15px;letter-spacing:.5px;color:var(--white)}

/* news */
.news-card{position:absolute;top:1847px;width:300px}
.date-badge{display:inline-block;background:var(--blue);color:var(--white);font-family:'Montserrat',sans-serif;font-size:12.5px;padding:7px 12px}
.news-card h4{margin-top:21px;font-family:'Montserrat',sans-serif;font-weight:700;font-size:15px;color:#111;white-space:nowrap}
.news-card p{margin-top:8px;font-size:13.5px;line-height:21.5px;color:#222}
.news-card a{display:inline-block;margin-top:10px;font-size:11.5px;font-weight:700;color:var(--blue);text-decoration:underline}
.chev{position:absolute}

/* cta */
.cta{position:absolute;left:0;top:2096px;width:1200px;height:262px;background:linear-gradient(90deg,#2e2e2e,#393939 50%,#262626)}
.cta h2{position:absolute;left:115px;top:75px;font-family:'Montserrat',sans-serif;font-size:35px;font-weight:700;color:var(--white)}
.cta p{position:absolute;left:115px;top:135px;width:420px;font-size:15px;line-height:25px;color:var(--white)}
.cta .btn-start{position:absolute;left:877px;top:106px;width:189px;height:51px;border:2px solid var(--white);color:var(--white);font-family:'Montserrat',sans-serif;font-weight:700;font-size:19px;letter-spacing:1px;text-align:center;line-height:47px}

/* partners */
.partner{position:absolute;top:2538px;width:141px;height:66px;border:1px solid #cfcfcf;background:var(--white)}
.partner.active{border-color:var(--blue)}
.partner i{position:absolute;left:45px;top:17px;width:50px;height:32px;border-radius:4px;background:#d9dde3}

/* footer */
.site-footer{position:absolute;left:0;top:2690px;width:1200px;height:294px;background:var(--footer)}
.f-head{position:absolute;top:56px;font-family:'Montserrat',sans-serif;font-size:17px;color:var(--white);letter-spacing:.5px}
.f-head::after{content:"";position:absolute;left:25px;top:30px;width:45px;height:2px;background:var(--blue)}
.f-divider{position:absolute;top:85px;width:1px;height:150px;background:#2a2a2a}
.f-links{position:absolute;left:115px;top:108px;list-style:none}
.f-links li{font-size:13px;color:var(--white);height:31.7px;padding-left:12px;position:relative}
.f-links li::before{content:"";position:absolute;left:0;top:8px;width:4px;height:4px;border-radius:50%;background:var(--blue)}
.f-contact{position:absolute;left:325px;font-size:12.5px;line-height:17px;color:var(--white)}
.f-contact svg{position:absolute;left:0;top:0}
.f-contact span{display:block;padding-left:28px}
.f-input{position:absolute;left:641px;width:225px;height:29px;background:var(--white);border:1px solid #999;font-size:11px;color:#888;padding:8px 9px}
.f-submit{position:absolute;left:641px;top:220px;width:104px;height:29px;background:var(--blue);color:var(--white);font-weight:700;font-size:13px;text-align:center;line-height:29px}
.social{position:absolute;left:980px;font-family:'Montserrat',sans-serif;font-size:12px;font-weight:500;color:var(--white)}
.social i{position:absolute;left:0;top:0;width:26px;height:26px;border:1px solid var(--white)}
.social span{position:absolute;left:36px;top:6px;white-space:nowrap}
.copyright{position:absolute;left:0;top:2984px;width:1200px;height:35px;background:var(--blue);color:var(--white);text-align:center;font-size:11.5px;line-height:35px}
</style>
</head>
<body>

<header class="site-header">
  <div class="brand"><i></i><span>Corventa Dx</span></div>
  <nav class="nav">
    <a class="active" style="left:429px" href="#">Home</a>
    <a style="left:539px" href="#">About Us</a>
    <a style="left:667px" href="#">Services</a>
    <a style="left:788px" href="#">Contact Us</a>
  </nav>
  <div class="header-divider"></div>
  <div class="call-label">Call Us Today</div>
  <div class="call-phone">123-456-7890</div>
</header>

<section class="hero" role="img" aria-label="Scientist in lab coat and safety goggles holding a test tube in a bright blue laboratory">
  <h1>We Are A Biotech Consulting Firm Serving The Medical Diagnostics Industry</h1>
  <div class="hero-arrow" style="left:112px"><svg width="10" height="12" viewBox="0 0 10 12"><path d="M7 1 2 6l5 5" fill="none" stroke="#111" stroke-width="2"/></svg></div>
  <div class="hero-arrow" style="left:150px"><svg width="10" height="12" viewBox="0 0 10 12"><path d="M3 1l5 5-5 5" fill="none" stroke="#111" stroke-width="2"/></svg></div>
</section>

<section class="welcome">
  <h2 class="sec-title" style="top:748px">Welcome To Corventa <em>Dx</em></h2>
  <div class="rule" style="top:796px"><i></i><i></i></div>
  <p class="lead" style="top:822px">Corventa Dx This Is A Consulting Firm That Will Serve Medical Diagnostics Industry,<br>Which Is Part of The Life Science/healthcare Industry</p>
  <p class="body-copy" style="top:882px">Lorem ipsum dolor sit amet, consectetuer adipiscing elit, sed diam nonummy nibh euismod tincidunt ut laoreet dolore magna aliquam erat volutpat. Ut wisi enim ad minim veniam, quis nostrud exerci tation ullamcorper suscipit lobortis nisl ut aliquip ex ea commodo consequat. Duis autem vel eum iriure or sit amet, consectetuer adipiscing elit, sed diam nonummy nibh euismod tincidunt ut laoreet dolore magna aliquam erat volutpat. Ut wisi enim</p>

  <div class="pillar-icon" style="left:183px;top:989px">
    <svg width="61" height="61" viewBox="0 0 61 61"><path d="M12 48 L30 20 L48 48 Z" fill="none" stroke="#111" stroke-width="1.6"/><path d="M30 20V10h8l-2 3 2 3h-8" fill="none" stroke="#111" stroke-width="1.6"/><path d="M22 40l5-4 5 3 5-4" fill="none" stroke="#111" stroke-width="1.4"/></svg>
  </div>
  <div class="pillar-title" style="left:262px;top:990px">MISSION</div>
  <p class="pillar-text" style="left:264px;top:1014px">Lorem ipsum dolor sit amet, consectetuer adipisci laoreet dolore magna aliquam erat volutpat.....<em>(+)</em></p>

  <div class="pillar-icon" style="left:639px;top:989px">
    <svg width="61" height="61" viewBox="0 0 61 61"><circle cx="36" cy="24" r="8" fill="none" stroke="#111" stroke-width="1.6"/><circle cx="36" cy="24" r="3" fill="#111"/><path d="M30 30 16 48M42 30l6 18M28 20l-10-4" fill="none" stroke="#111" stroke-width="1.6"/><path d="M18 12l2 2M22 10v3" stroke="#111" stroke-width="1.4"/></svg>
  </div>
  <div class="pillar-title" style="left:718px;top:990px">VISION</div>
  <p class="pillar-text" style="left:720px;top:1014px">Lorem ipsum dolor sit amet, consectetuer adipisci laoreet dolore magna aliquam erat volutpat.....<em>(+)</em></p>
</section>

<section class="services" role="img" aria-label="Blue tinted photo of a hand writing with a pen on paper">
  <h2 class="sec-title">Our <em>Services</em></h2>
  <div class="rule" style="top:125px"><i></i><i></i></div>
  <p class="sub">Our Consulting Firm Will Help Medical Diagnostic Companies To Overcome Key Challenges In</p>

  <div class="service" style="left:88px">
    <svg width="66" height="68" viewBox="0 0 66 68" fill="none" stroke="#fff" stroke-width="2"><rect x="4" y="54" width="58" height="8"/><rect x="10" y="14" width="10" height="40"/><rect x="24" y="6" width="8" height="48"/><rect x="36" y="10" width="8" height="44"/><rect x="48" y="18" width="8" height="36"/><path d="M28 14v6M40 18v6M52 26v6"/></svg>
    <h3>Designing</h3>
    <p>Lorem ipsum dolor sit amet, consectetuer adipiscing elit , sed diam nonummy nibh</p>
    <span class="btn-outline">READ MORE</span>
  </div>
  <div class="service" style="left:441px">
    <svg width="80" height="72" viewBox="0 0 80 72" fill="none" stroke="#fff" stroke-width="2"><rect x="6" y="8" width="46" height="60"/><rect x="20" y="3" width="18" height="8"/><circle cx="36" cy="34" r="11"/><path d="M31 34l4 4 7-8M44 42l12 12M12 24h8M12 36h8M12 48h8M12 58h26"/><path d="M70 4l3 3-3 3-3-3z"/></svg>
    <h3>Evaluating</h3>
    <p>Lorem ipsum dolor sit amet, consectetuer adipiscing elit , sed diam nonummy nibh</p>
    <span class="btn-outline">READ MORE</span>
  </div>
  <div class="service" style="left:797px">
    <svg width="96" height="68" viewBox="0 0 96 68" fill="none" stroke="#fff" stroke-width="2"><rect x="4" y="6" width="54" height="40"/><path d="M24 46v10M14 58h22"/><path d="M12 16l10 6-10 6z"/><path d="M46 20h10l18-12v36L56 32H46z"/><path d="M82 14l6-4M84 26h8M82 38l6 4"/><path d="M12 36h20"/></svg>
    <h3>Marketing New Products</h3>
    <p>Lorem ipsum dolor sit amet, consectetuer adipiscing elit , sed diam nonummy nibh</p>
    <span class="btn-outline">READ MORE</span>
  </div>
</section>

<section class="news">
  <h2 class="sec-title" style="top:1757px">Latest <em>News</em></h2>
  <div class="rule" style="top:1804px"><i></i><i></i></div>
  <svg class="chev" style="left:60px;top:1932px" width="16" height="30" viewBox="0 0 16 30"><path d="M14 2 3 15l11 13" fill="none" stroke="#999" stroke-width="2.5"/></svg>
  <svg class="chev" style="left:1124px;top:1932px" width="16" height="30" viewBox="0 0 16 30"><path d="M2 2l11 13L2 28" fill="none" stroke="#999" stroke-width="2.5"/></svg>
  <article class="news-card" style="left:114px">
    <span class="date-badge">JUNE 05, 2019</span>
    <h4>LOREM IPSUM DOLOR SIT AMET NSE</h4>
    <p>Quis nostrud exerci tation ullamcorper suscipit lobortis nisl ut aliquip ex ea commodonsequat Duis autem vel eum iriure</p>
    <a href="#">LEARN MORE</a>
  </article>
  <article class="news-card" style="left:459px">
    <span class="date-badge">JUNE 05, 2019</span>
    <h4>SED DIAM NONUMMY NIBH EUISMOD</h4>
    <p>Quis nostrud exerci tation ullamcorper suscipit lobortis nisl ut aliquip ex ea commodonsequat Duis autem vel eum iriure</p>
    <a href="#">LEARN MORE</a>
  </article>
  <article class="news-card" style="left:805px">
    <span class="date-badge">JUNE 05, 2019</span>
    <h4>LOREM IPSUM DOLOR SIT AMET NSE</h4>
    <p>Quis nostrud exerci tation ullamcorper suscipit lobortis nisl ut aliquip ex ea commodonsequat Duis autem vel eum iriure</p>
    <a href="#">LEARN MORE</a>
  </article>
</section>

<section class="cta" role="img" aria-label="Dark photo of a researcher looking into a microscope">
  <h2>Not Sure of Your Next Step?</h2>
  <p>Lorem ipsum dolor sit amet, consectetuer adipiscing elit, sed nonummy nibh euismod tincidunt ut laoreet dolore</p>
  <div class="btn-start">GET STARTED</div>
</section>

<section class="partners">
  <h2 class="sec-title" style="top:2456px">Our <em>Partners</em></h2>
  <div class="rule" style="top:2505px"><i></i><i></i></div>
  <svg class="chev" style="left:50px;top:2556px" width="18" height="36" viewBox="0 0 18 36"><path d="M16 2 3 18l13 16" fill="none" stroke="#bbb" stroke-width="2"/></svg>
  <svg class="chev" style="left:1117px;top:2556px" width="18" height="36" viewBox="0 0 18 36"><path d="M2 2l13 16L2 34" fill="none" stroke="#888" stroke-width="2"/></svg>
  <div class="partner active" style="left:112px"><i></i></div>
  <div class="partner" style="left:279px"><i></i></div>
  <div class="partner" style="left:445px"><i></i></div>
  <div class="partner" style="left:612px"><i></i></div>
  <div class="partner" style="left:779px"><i></i></div>
  <div class="partner" style="left:945px"><i></i></div>
</section>

<footer class="site-footer">
  <div class="f-head" style="left:115px">Quick Links</div>
  <div class="f-head" style="left:325px">Contact Details</div>
  <div class="f-head" style="left:639px">Quick Inquiry</div>
  <div class="f-head" style="left:976px">Follow Us</div>
  <div class="f-divider" style="left:268px"></div>
  <div class="f-divider" style="left:583px"></div>
  <div class="f-divider" style="left:921px"></div>

  <ul class="f-links">
    <li>Home</li><li>About Us</li><li>Services</li><li>Contact Us</li>
  </ul>

  <div class="f-contact" style="top:109px">
    <svg width="14" height="18" viewBox="0 0 14 18"><path d="M7 1a6 6 0 0 1 6 6c0 4-6 10-6 10S1 11 1 7a6 6 0 0 1 6-6z" fill="none" stroke="#2f86ea" stroke-width="2"/><circle cx="7" cy="7" r="2" fill="#2f86ea"/></svg>
    <span>123 Loren Ipsum dolor mnwp<br>AB Mnwrr Conr 1234</span>
  </div>
  <div class="f-contact" style="top:164px">
    <svg width="16" height="16" viewBox="0 0 16 16"><path d="M3 1l3 3-2 2c1 2 4 5 6 6l2-2 3 3-2 2C7 15 1 9 1 3z" fill="#2f86ea"/></svg>
    <span>123-456-7890</span>
  </div>
  <div class="f-contact" style="top:208px">
    <svg width="16" height="12" viewBox="0 0 16 12"><rect x="0" y="0" width="16" height="12" rx="1" fill="#2f86ea"/><path d="M1 1l7 6 7-6" fill="none" stroke="#121212" stroke-width="1.3"/></svg>
    <span>info@corventadx.com</span>
  </div>

  <div class="f-input" style="top:112px">Name</div>
  <div class="f-input" style="top:147px">Email</div>
  <div class="f-input" style="top:184px">Message</div>
  <div class="f-submit">Submit</div>

  <div class="social" style="top:113px"><i></i><span>FRIENDSHEET</span></div>
  <div class="social" style="top:159px"><i></i><span>CHIRPLINE</span></div>
  <div class="social" style="top:205px"><i></i><span>WORKLINK</span></div>
</footer>

<div class="copyright">Copyright © 2019 Corventa Dx . All Rights Reserved.</div>

</body>
</html>
```